Label design - Superfood blend

We are a family owned nutrition company with big ambitions. Our goal is to develop a range of 100% natural supplements for women, inspired by nature & modern technology that helps them meet their nutritional needs while nourishing them from within. All our products are junk free because we believe that that’s how nature intended it. We also produce products through a sustainable process and only use biodegradable packaging for our products (See link - https://www.pouchwerk.example.uk/biodegradable-stand-pouch-250g-kraft)

Our brand style is modern and minimalist. This same style will be reflected in our social media, website and we want it to be represented through the label designs for our product packaging.

We want some creative designers to design a label that is true to our style (See attached packaging brief with designs we like) and displays our values of Premium, High Quality, Organic Real Food supplements focused on women. I have provided examples in the attached brief, but please only use as inspiration, I dont want any of them to be copied (sorry have had my fingers burnt already !)

Need extra days to review

Hello all, Please note this design is for a LABEL and not the whole package. We will have a 500gm biodegradable brown package, and we will have a label (which is what this project is about) that will be stuck on the front. The size of the label will be a rectangle (unless you come up with a new shape) in the size 20cm * 15cm. Please do not submit designs for the WHOLE from of the package, as we dont intend to have printed packages. Regards

Hello all, I have added a new logo version to the attachments, could you please also try that version. Could you also please look at the new sliders. We are only looking for a minimlaist theme. If you dont know what that means, please do feel free to ask, I would be happy to supply examples. Minimalist designs, means clean, modern, upmarket, elegant designs. It does not use too many colors and mostly sticks to a combination of black and white with colors used sparingly. See some below for your reference anyway. https://www.artbidhub.example.uk/design/48120573 https://www.artbidhub.example.uk/design/52961804 https://www.artbidhub.example.uk/design/47305916 https://www.artbidhub.example.uk/design/46719258 https://www.snapboardly.example.com/search/pins/?q=minimalist%20label%20design&rs=rs&eq=&etslf=2809&term_meta[]=minimalist%7Crecentsearch%7Cundefined&term_meta[]=label%7Crecentsearch%7Cundefined&term_meta[]=design%7Crecentsearch%7Cundefined Regards

Target Market(s)

The target market is women between the age 25 to 45, based in UK (mostly based in larger cities in UK). They are typically middle class or higher and would be in demanding jobs and social lives, that requires for them to meet their nutrition needs in convenient, easy to take forms. The women would also be socially conscious and sensitive to issues like women's rights, environmental issues, healthy food, organic food and sustainability etc. I have a much more detailed customer avatar if required

Font styles to use
Serif
Sans Serif
Decorative
Script

Colors
e8e8e8
474747
1b1b1b
add136

Requirements
Must have
• The label, should look minimalist and modern, throw in some out of the box creativity and we have a winner. Creativity will definitely be of importance. Our packaging is a biodegradable brown paper stand up pouch (Example link in product description). So to make it standout from other colorful packaging - being creative would definitely help.
• Please use the color schemes provided in the brief (See attachments). But if you want to experiment I would be open to it, as long as they are still minimalist and does not stray very far from the color given in the brief :)

```html
<!DOCTYPE html>
<html lang="en">
<head>
<meta charset="utf-8">
<title>Verdalune – Rooted Daily label</title>
<link rel="stylesheet" href="https://fonts.googleapis.com/css2?family=Josefin+Sans:wght@300;400&family=Playfair+Display:wght@400;500;700&display=swap">
<style>
  :root {
    --backdrop: #efede8;
    --label-white: #ffffff;
    --leaf-green: #5b7a2c;
    --ink: #2f2f2f;
    --rule-green: #7d9650;
  }
  * { margin: 0; padding: 0; box-sizing: border-box; }
  html, body {
    width: 1200px;
    height: 901px;
    overflow: hidden;
    background: var(--backdrop);
  }
  .label {
    position: absolute;
    left: 285px;
    top: 30px;
    width: 630px;
    height: 840px;
    background: var(--label-white);
    box-shadow: 0 2px 10px rgba(0,0,0,0.08);
    font-family: 'Playfair Display', Georgia, serif;
    text-align: center;
  }
  .label__frame {
    position: absolute;
    inset: 14px;
    border: 1.5px solid var(--leaf-green);
  }
  .brand {
    position: absolute;
    top: 80px;
    left: 0;
    right: 0;
    display: flex;
    flex-direction: column;
    align-items: center;
    gap: 34px;
  }
  .brand__dot {
    width: 22px;
    height: 22px;
    border-radius: 50%;
    background: var(--leaf-green);
  }
  .brand__name {
    font-family: 'Josefin Sans', Arial, sans-serif;
    font-weight: 400;
    font-size: 36px;
    letter-spacing: 8px;
    color: var(--ink);
    padding-left: 8px;
  }
  .product-name {
    position: absolute;
    top: 290px;
    left: 0;
    right: 0;
    height: 320px;
    display: flex;
    flex-direction: column;
    justify-content: center;
    align-items: center;
    color: var(--leaf-green);
    font-weight: 500;
    font-size: 92px;
    line-height: 100px;
    letter-spacing: 1px;
  }
  .product-type {
    position: absolute;
    top: 648px;
    left: 0;
    right: 0;
    color: var(--leaf-green);
    font-weight: 500;
    font-size: 34px;
    line-height: 44px;
    letter-spacing: 0.5px;
  }
  .rule {
    position: absolute;
    left: 110px;
    right: 110px;
    border-top: 1.5px dashed var(--rule-green);
  }
  .rule--upper { top: 700px; }
  .rule--lower { top: 762px; }
  .product-desc {
    position: absolute;
    top: 707px;
    left: 0;
    right: 0;
    color: var(--leaf-green);
    font-size: 14px;
    line-height: 24px;
    letter-spacing: 0.6px;
  }
  .net-weight {
    position: absolute;
    top: 774px;
    left: 0;
    right: 0;
    color: var(--ink);
  }
  .net-weight__caption {
    display: block;
    font-size: 12px;
    line-height: 16px;
    letter-spacing: 1px;
  }
  .net-weight__value {
    display: block;
    font-size: 20px;
    line-height: 26px;
    font-weight: 700;
  }
  .cert-badge {
    position: absolute;
    top: 774px;
    width: 42px;
    height: 42px;
    border-radius: 50%;
  }
  .cert-badge--vegan { left: 128px; background: var(--leaf-green); }
  .cert-badge--organic { right: 128px; border: 2px solid var(--ink); }
</style>
</head>
<body>
  <main class="label">
    <div class="label__frame"></div>

    <header class="brand">
      <span class="brand__dot"></span>
      <span class="brand__name">VERDALUNE</span>
    </header>

    <h1 class="product-name">
      <span>ROOTED</span>
      <span>DAILY</span>
    </h1>

    <p class="product-type">FOOD SUPPLEMENT</p>
    <div class="rule rule--upper"></div>
    <p class="product-desc">ORGANIC, PLANT-BASED PREBIOTICS<br>AND SUPERFOOD BLEND</p>
    <div class="rule rule--lower"></div>

    <span class="cert-badge cert-badge--vegan" role="img" aria-label="Vegan certification badge"></span>
    <p class="net-weight">
      <span class="net-weight__caption">NET WEIGHT</span>
      <span class="net-weight__value">18 oz (500 g)</span>
    </p>
    <span class="cert-badge cert-badge--organic" role="img" aria-label="Organic certification badge"></span>
  </main>
</body>
</html>
```